Business card for technical support company.
FixWiseDesk.com
Business card for technical support company.  - Computers
Creative Brief
Use specific fonts
Up To designer
Professional
Marcus Bell
VP In Charge
482 Alder Lane New York, NY 48213
service@FixWiseDesk.com
This will be used as a mock-up for my business card. Editable Adobe Illustrator or comparable original design file will need to be included with the final design. Also logo can be broken up from the FixWiseDesk.com below it and arranged on the card.
Company logo, website, and possible list of services. Please allow room to add later. 5-6 bullet points
qm71xrb qm71xrb
Nice first drafts everyone. I would like to see how some of these look with a white background instead of black. Nice!
I would like one design but two separate color schemes. Please match the two color schemes of the example logos provided. Thank you!

```html
<!DOCTYPE html>
<html lang="en">
<head>
<meta charset="utf-8">
<title>FixWiseDesk – Business Card</title>
<link href="https://fonts.googleapis.com/css2?family=Montserrat:wght@400;600;700&display=swap" rel="stylesheet">
<style>
  :root{
    --page:#e4e6e8;
    --card-light:#ffffff;
    --card-dark:#343536;
    --ink-dark:#2b3440;
    --brand-blue:#1f78d6;
    --brand-deep:#0c3e86;
    --silver:#b9bec4;
    --text-light:#e6e8ea;
    --text-muted:#a9adb2;
  }
  *{box-sizing:border-box;margin:0;padding:0}
  html,body{width:1200px;height:946px;overflow:hidden;background:var(--page)}
  body{font-family:"Montserrat",Arial,sans-serif;position:relative}

  .card{
    position:absolute;left:220px;width:760px;height:434px;
    border-radius:26px;overflow:hidden;
    box-shadow:0 10px 24px rgba(0,0,0,.18);
  }
  .card--front{top:26px;background:var(--card-light)}
  .card--back{top:486px;background:var(--card-dark)}

  .brand{
    position:absolute;display:flex;align-items:center;gap:14px;
  }
  .brand__mark{width:34px;height:34px;border-radius:4px}
  .brand__name{font-weight:700;font-size:30px;letter-spacing:.04em;text-transform:uppercase}

  .card--front .brand{left:50%;top:50%;transform:translate(-50%,-50%)}
  .card--front .brand__mark{background:var(--brand-blue)}
  .card--front .brand__name{color:var(--ink-dark)}

  .card--back .brand{left:60px;top:150px}
  .card--back .brand__mark{background:var(--brand-blue)}
  .card--back .brand__name{color:var(--text-light);font-size:28px}

  .divider{position:absolute;left:418px;top:112px;width:1px;height:198px;background:var(--text-muted);opacity:.6}

  .contact{position:absolute;left:444px;top:108px;color:var(--text-light)}
  .contact__name{font-weight:600;font-size:15px;letter-spacing:.12em;text-transform:uppercase}
  .contact__title{font-size:12px;color:var(--text-muted);margin-top:4px}
  .contact__address{font-size:12px;line-height:1.5;margin-top:16px;color:var(--text-light)}
  .contact__list{list-style:none;margin-top:16px}
  .contact__item{display:flex;align-items:center;gap:10px;font-size:11.5px;line-height:1;margin-bottom:9px}
  .contact__icon{width:13px;height:13px;flex:none;fill:none;stroke:var(--text-light);stroke-width:1.6}

  .swoosh{position:absolute;left:0;bottom:0;width:760px;height:434px}
</style>
</head>
<body>

<section class="card card--front" aria-label="Card front">
  <div class="brand">
    <span class="brand__mark"></span>
    <span class="brand__name">FixWiseDesk</span>
  </div>
</section>

<section class="card card--back" aria-label="Card back">
  <svg class="swoosh" viewBox="0 0 760 434" aria-hidden="true">
    <defs>
      <linearGradient id="swooshBlue" x1="0" y1="0" x2="1" y2="0">
        <stop offset="0" stop-color="#0c3e86"/>
        <stop offset=".35" stop-color="#2a8cf0"/>
        <stop offset=".7" stop-color="#1f78d6"/>
        <stop offset="1" stop-color="#0c3e86"/>
      </linearGradient>
      <linearGradient id="swooshSilver" x1="0" y1="0" x2="1" y2="0">
        <stop offset="0" stop-color="#8e949a"/>
        <stop offset=".45" stop-color="#e8ebee"/>
        <stop offset="1" stop-color="#6e7378"/>
      </linearGradient>
    </defs>
    <path d="M0 318 C 150 372, 420 396, 760 372 L760 434 L0 434 Z" fill="url(#swooshSilver)" opacity=".55"/>
    <path d="M0 334 C 170 384, 440 404, 760 386 L760 434 L0 434 Z" fill="url(#swooshBlue)"/>
    <path d="M0 334 C 170 384, 440 404, 760 386" fill="none" stroke="#7fc0ff" stroke-width="1.5" opacity=".8"/>
  </svg>

  <div class="brand">
    <span class="brand__mark"></span>
    <span class="brand__name">FixWiseDesk</span>
  </div>

  <div class="divider"></div>

  <div class="contact">
    <p class="contact__name">Marcus Bell</p>
    <p class="contact__title">VP In Charge</p>
    <p class="contact__address">482 Alder Lane<br>New York, NY 48213</p>
    <ul class="contact__list">
      <li class="contact__item">
        <svg class="contact__icon" viewBox="0 0 16 16"><path d="M3 2h3l1 3-2 1a8 8 0 0 0 5 5l1-2 3 1v3a1 1 0 0 1-1 1A12 12 0 0 1 2 3a1 1 0 0 1 1-1z"/></svg>
        <span>555 210 4821</span>
      </li>
      <li class="contact__item">
        <svg class="contact__icon" viewBox="0 0 16 16"><rect x="4" y="1.5" width="8" height="13" rx="1.5"/><path d="M7 12h2"/></svg>
        <span>555 370 1948</span>
      </li>
      <li class="contact__item">
        <svg class="contact__icon" viewBox="0 0 16 16"><rect x="1.5" y="3.5" width="13" height="9" rx="1"/><path d="M1.5 4l6.5 5 6.5-5"/></svg>
        <span>service@FixWiseDesk.com</span>
      </li>
      <li class="contact__item">
        <svg class="contact__icon" viewBox="0 0 16 16"><circle cx="8" cy="8" r="6.5"/><path d="M1.5 8h13M8 1.5c2.5 2.5 2.5 10.5 0 13M8 1.5c-2.5 2.5-2.5 10.5 0 13"/></svg>
        <span>www.FixWiseDesk.com</span>
      </li>
    </ul>
  </div>
</section>

</body>
</html>
```